I need the design of a label for wine bottles, the design I leave at the free choice of the designer, it must contain the name of the winery that is: "Bodegas RT"

Bodegas RT

```html
<!DOCTYPE html>
<html lang="en">
<head>
<meta charset="utf-8">
<title>Bodegas RT — Chardonnay label</title>
<link rel="stylesheet" href="https://fonts.googleapis.com/css2?family=Open+Sans:wght@300;400&family=Pinyon+Script&display=swap">
<style>
  :root {
    --backdrop: #c9cacc;
    --teal: #234447;
    --black: #000000;
    --bar-grey: #808080;
    --line-grey: #c8c8c8;
    --text-white: #ffffff;
    --mark-grey: #cfcfcf;
  }
  * { margin: 0; padding: 0; box-sizing: border-box; }
  html, body { width: 1200px; height: 1023px; overflow: hidden; }
  body {
    position: relative;
    background: var(--backdrop);
    font-family: "Open Sans", Arial, sans-serif;
  }

  /* Neck label */
  .neck-label {
    position: absolute;
    left: 513px; top: 0;
    width: 174px; height: 375px;
    background: var(--teal);
  }
  .neck-label__bar {
    position: absolute;
    left: 60px; top: 0;
    width: 52px; height: 228px;
    background: var(--bar-grey);
  }
  .neck-label__name {
    position: absolute;
    left: 0; right: 0; top: 282px;
    text-align: center;
    font-weight: 400;
    font-size: 17px;
    letter-spacing: 2px;
    color: var(--mark-grey);
  }

  /* Front label */
  .front-label {
    position: absolute;
    left: 310px; top: 402px;
    width: 581px; height: 621px;
    background: var(--teal);
    overflow: hidden;
  }
  .front-label__mark-name {
    position: absolute;
    left: 0; right: 0; top: 62px;
    text-align: center;
    font-weight: 400;
    font-size: 30px;
    letter-spacing: 3px;
    color: var(--black);
  }
  .front-label__panel {
    position: absolute;
    left: 0; top: 169px;
    width: 581px; height: 407px;
    background: var(--black);
  }
  .front-label__rays {
    position: absolute;
    left: 0; top: 6px;
    width: 581px; height: 246px;
    background:
      radial-gradient(ellipse 420px 240px at 100% 100%,
        rgba(200,200,200,0.55) 0%,
        rgba(140,140,140,0.28) 35%,
        rgba(60,60,60,0.12) 70%,
        rgba(0,0,0,0) 100%);
  }
  .front-label__winery {
    position: absolute;
    left: 0; right: 0; top: 114px;
    text-align: center;
    font-weight: 400;
    font-size: 46px;
    letter-spacing: 9px;
    color: var(--text-white);
  }
  .front-label__variety-row {
    position: absolute;
    left: 0; right: 0; top: 280px;
    height: 60px;
  }
  .front-label__rule {
    position: absolute;
    top: 30px;
    height: 2px;
    background: var(--line-grey);
  }
  .front-label__rule--left { left: 0; width: 169px; }
  .front-label__rule--right { left: 414px; width: 167px; }
  .front-label__variety {
    position: absolute;
    left: 169px; width: 245px; top: 0;
    text-align: center;
    font-family: "Pinyon Script", cursive;
    font-size: 50px;
    line-height: 60px;
    color: var(--line-grey);
  }
  .front-label__base-line {
    position: absolute;
    left: 0; top: 576px;
    width: 581px; height: 3px;
    background: var(--bar-grey);
  }
</style>
</head>
<body>
  <div class="neck-label">
    <div class="neck-label__bar"></div>
    <div class="neck-label__name">Bodegas RT</div>
  </div>

  <div class="front-label">
    <div class="front-label__mark-name">Bodegas RT</div>
    <div class="front-label__panel">
      <div class="front-label__rays" role="img" aria-label="Fan of fine light rays radiating from the lower right corner"></div>
      <div class="front-label__winery">Bodegas RT</div>
      <div class="front-label__variety-row">
        <span class="front-label__rule front-label__rule--left"></span>
        <span class="front-label__variety">Chardonnay</span>
        <span class="front-label__rule front-label__rule--right"></span>
      </div>
    </div>
    <div class="front-label__base-line"></div>
  </div>
</body>
</html>
```